Medical Skincare services/menu/pricing Booklet 12 pages

We need produce a 12-page glossy, saddle-stitched booklet (5 1/2" tall X 81/2" wide). The booklet will be used as a services menu for a skin care salon. I have mocked up the booklet (w/ all copy) in WORD and I've provided a separate PDF of the accurate page order (see files attached). IMPORTANT: Feel free to use your creativity yet style-wise it should kinda match my wife's website colors and text style. Her clients are demanding so she wants a clean, high end, modern look (ala Pebble maybe?). See her website for a frame of reference www.GlowWithMarta.com

Target Market(s)

upscale female, professional women, teens with acne

Industry/Entity Type

Medical

Requirements
Must have
• the pics in the mock up are important. I've attached them here

```html
<!DOCTYPE html>
<html lang="en">
<head>
<meta charset="utf-8">
<title>Glow with Marta — Services</title>
<link rel="stylesheet" href="https://fonts.googleapis.com/css2?family=Open+Sans:wght@300&display=swap">
<style>
  :root {
    --ink: #000000;
    --brand: #ffffff;
    --menu: #b5b5b5;
  }
  html, body {
    margin: 0;
    padding: 0;
    width: 1200px;
    height: 777px;
    overflow: hidden;
    background: var(--ink);
  }
  .cover {
    position: relative;
    width: 1200px;
    height: 777px;
    background: var(--ink);
  }
  .brand-name {
    position: absolute;
    left: 36px;
    top: 346px;
    margin: 0;
    font-family: "Open Sans", "Myriad Pro", sans-serif;
    font-weight: 300;
    font-size: 62px;
    line-height: 80px;
    letter-spacing: 1px;
    color: var(--brand);
    white-space: nowrap;
  }
  .service-list {
    position: absolute;
    right: 35px;
    top: 334px;
    margin: 0;
    padding: 0;
    list-style: none;
    text-align: right;
    font-family: "Open Sans", "Myriad Pro", sans-serif;
    font-weight: 300;
    font-size: 30px;
    line-height: 41.2px;
    color: var(--menu);
  }
  .service-list .indent { padding-right: 8px; }
</style>
</head>
<body>
  <main class="cover">
    <h1 class="brand-name">Glow with Marta</h1>
    <ul class="service-list">
      <li>HydroLift MD</li>
      <li>Laser Renewal</li>
      <li>IPL (Brightwave)</li>
      <li>Vascular</li>
      <li>Microneedling MD</li>
      <li class="indent">LED Light Therapy</li>
      <li>Vita Peel</li>
      <li>Customized</li>
      <li class="indent">Facials &amp; Peels</li>
      <li>Dermaplane</li>
    </ul>
  </main>
</body>
</html>
```